Mesh Banner Design for Business Premises

We require the design of a large mesh banner to be installed across the front fence of our warehouse. The banner should prominently feature our existing Rigmore logo and brand colours (yellow, white, and black) and be designed to be highly visible from the road.

The overall aesthetic should be strong, masculine, and industrial, reflecting the nature of the scaffolding and construction industry. The background should be predominantly black, with our branding incorporated in yellow and white for strong contrast and readability.

The banner should clearly communicate the full scope of services we provide, including:

Scaffold Design
Scaffold Engineering
Scaffold Installation / Erection
Scaffold Dismantling

It should also indicate the types of projects and clients we service, including:

Commercial
Industrial
Residential
Civil

The design should feel bold and professional, with a construction-oriented style that aligns with the scaffolding industry. It should be clean, impactful, and easy to read from a distance, ensuring passing traffic can quickly understand our services.

Where possible, subtle industrial or structural design elements (such as scaffold components, steel textures, or linework) may be incorporated into the background to reinforce the industry theme while keeping the layout uncluttered.

The final design will be produced as a large-format mesh banner for outdoor installation, so it should be created with this application and viewing distance in mind.

```html
<!DOCTYPE html>
<html lang="en">
<head>
<meta charset="utf-8">
<title>Rigmore – Fence Banner</title>
<link rel="stylesheet" href="https://fonts.googleapis.com/css2?family=Michroma&display=swap">
<style>
  :root {
    --page-bg: #d9d9d9;
    --banner-bg: #f2f2f2;
    --brand-yellow: #e5ab2c;
    --ink: #121212;
  }
  * { margin: 0; padding: 0; box-sizing: border-box; }
  html, body {
    width: 1200px;
    height: 864px;
    overflow: hidden;
    background: var(--page-bg);
    font-family: "Michroma", "Arial", sans-serif;
    color: var(--ink);
  }
  .banner {
    position: absolute;
    left: 0;
    top: 132px;
    width: 1200px;
    height: 600px;
    background: var(--banner-bg);
    overflow: hidden;
  }
  .hazard-band {
    position: absolute;
    left: 0;
    top: 0;
    width: 1200px;
    height: 118px;
    display: block;
  }
  .hazard-band polygon { fill: var(--brand-yellow); }

  .brand-mark {
    position: absolute;
    left: 48px;
    top: 175px;
    width: 400px;
    height: 294px;
    display: flex;
    align-items: center;
    justify-content: center;
    gap: 18px;
  }
  .brand-mark__square {
    width: 34px;
    height: 34px;
    background: var(--brand-yellow);
  }
  .brand-mark__name {
    font-size: 38px;
    letter-spacing: 0.12em;
    color: var(--brand-yellow);
  }
  .phone {
    position: absolute;
    left: 48px;
    width: 400px;
    top: 496px;
    text-align: center;
    font-size: 19px;
    letter-spacing: 0.32em;
  }

  .company-name {
    position: absolute;
    left: 558px;
    top: 166px;
    font-size: 36px;
    letter-spacing: 0.62em;
    line-height: 1;
  }
  .services {
    position: absolute;
    left: 560px;
    top: 250px;
    list-style: none;
  }
  .services li {
    position: relative;
    height: 52px;
    padding-left: 31px;
    font-size: 15.5px;
    letter-spacing: 3px;
    line-height: 34px;
  }
  .services li::before {
    content: "";
    position: absolute;
    left: 0;
    top: 1px;
    width: 0;
    height: 0;
    border-top: 16px solid transparent;
    border-bottom: 16px solid transparent;
    border-left: 17px solid var(--brand-yellow);
  }
  .sectors {
    position: absolute;
    left: 560px;
    top: 484px;
    width: 583px;
    height: 49px;
    background: var(--brand-yellow);
    display: flex;
    align-items: center;
    justify-content: center;
    font-size: 11px;
    letter-spacing: 2.6px;
    white-space: nowrap;
  }
</style>
</head>
<body>
  <main class="banner">
    <svg class="hazard-band" viewBox="0 0 1724 170" preserveAspectRatio="none" aria-hidden="true">
      <polygon points="-74,170 2,170 112,0 36,0"/>
      <polygon points="52,170 128,170 238,0 162,0"/>
      <polygon points="178,170 254,170 364,0 288,0"/>
      <polygon points="304,170 380,170 490,0 414,0"/>
      <polygon points="430,170 506,170 616,0 540,0"/>
      <polygon points="556,170 632,170 742,0 666,0"/>
      <polygon points="682,170 758,170 868,0 792,0"/>
      <polygon points="808,170 884,170 994,0 918,0"/>
      <polygon points="934,170 1010,170 1120,0 1044,0"/>
      <polygon points="1060,170 1136,170 1246,0 1170,0"/>
      <polygon points="1186,170 1262,170 1372,0 1296,0"/>
      <polygon points="1312,170 1388,170 1498,0 1422,0"/>
      <polygon points="1438,170 1514,170 1624,0 1548,0"/>
      <polygon points="1564,170 1640,170 1750,0 1674,0"/>
      <polygon points="1690,170 1766,170 1876,0 1800,0"/>
    </svg>

    <div class="brand-mark">
      <span class="brand-mark__square"></span>
      <span class="brand-mark__name">RIGMORE</span>
    </div>
    <p class="phone">1300 9 RAISE</p>

    <h1 class="company-name">RIGMORE</h1>
    <ul class="services">
      <li>SCAFFOLD DESIGN</li>
      <li>SCAFFOLD ENGINEERING</li>
      <li>SCAFFOLD INSTALLATION/ERECTION</li>
      <li>SCAFFOLD DISMANTLING</li>
    </ul>
    <p class="sectors">COMMERCIAL&nbsp;&nbsp;|&nbsp;&nbsp;INDUSTRIAL&nbsp;&nbsp;|&nbsp;&nbsp;RESIDENTIAL&nbsp;&nbsp;|&nbsp;&nbsp;CIVIL</p>
  </main>
</body>
</html>
```